Eyecatching website design for commercial lighting business

This contest is all about the graphic design aspect. We need a striking website design for a commercial lighting company. We want something really eye catching to introduce people to our range of induction and LED lights which save businesses money on maintenance and electricity costs.

To be successful in this contest you will need to provide a design and pictures for the pages listed below.

We are using the platform vorada.com.au and you can see the attached template which everything will be loaded into so we just need HTML files which we can upload and we can do everything else from Vorada.

The final design should be strong and clean and use the colours and textures in the attached business card file.

Detailed requirements:

Please see attached screenshot of the website template, all we need is a fantastic graphic design and improvement/ incorporation of our logo for the following pages
Page Headings:
1. Home
About Us, Contact Us, snapshot of and link to Blog

Each of the below pages will have several paragraphs of text followed by a list of suitable products which is generated from our product catalogue.

2. Car Park Lighting
3. Educational Lighting
4. Hospitality Lighting
5. Office & Shop Lighting
6. Warehouse Lighting

Some of the website we have seen which are similar in nature are:
http://www.quillbeam.com.au/
http://www.oviron.com/
http://www.plankhollow.net/commercial-led
but we really want a modern, eye catching and memorable design

Some of the designs built on Vorada that we like are:

http://www.tenmilebarrow.com.au/
http://www.pebblecrate.com.au/
http://www.wexmantle.com.au/

I've also uploaded a couple of photos that we love. We'd like something similar for each industry.

Target Market(s)

Company Owners, Maintenance & Facilities Managers, Electrical Contractors

Industry/Entity Type

Electrical

Coding

Coded - Design and coding required

Number of Pages Required

5+ page

Font styles to use
Sans Serif

Colors
33a6d7
ec1f27

Requirements
Must have
• -Must scale to mobile
• -HTML coded files need to be provided (HTML Bootstrap)
Nice to have
• -Prefer incorporation of our logo into header bar
• -Design of 2-3 advertising banners which can be displayed on the home page
• -Prominent call to action button towards top of page 'Get a quote' or similar
• -Grid based design HTML Bootstrap

```html
<!DOCTYPE html>
<html lang="en">
<head>
<meta charset="utf-8">
<title>Lumvale – Commercial Lighting</title>
<link rel="stylesheet" href="https://fonts.googleapis.com/css2?family=Open+Sans:wght@300;400;600;700;800&display=swap">
<style>
:root{
  --blue:#33a6d7;
  --red:#ec1f27;
  --ink:#1c1d21;
  --dark:#232428;
  --darker:#16171a;
  --grey:#f1f1f1;
  --mid:#8a8d93;
  --text:#4a4d52;
  --white:#ffffff;
}
*{box-sizing:border-box;margin:0;padding:0}
html,body{width:1200px;height:2600px;overflow:hidden}
body{font-family:"Open Sans",Arial,sans-serif;color:var(--text);background:var(--white);font-size:13px}
.container{width:960px;margin:0 auto;position:relative}
.btn{display:inline-block;background:var(--ink);color:var(--white);font-size:11px;font-weight:600;padding:6px 12px;border-radius:2px}
.eyebrow{font-size:12px;font-weight:700;letter-spacing:1px;color:var(--blue);text-transform:uppercase}
.heading{font-size:44px;font-weight:300;letter-spacing:1px;text-transform:uppercase;color:var(--ink);line-height:1}

/* header */
.site-header{height:120px}
.site-header .container{height:120px;display:flex;align-items:center;justify-content:space-between}
.brand{display:flex;align-items:center;gap:12px}
.brand-square{width:40px;height:40px;background:var(--ink)}
.brand-name{font-size:30px;font-weight:600;color:var(--ink);line-height:1;white-space:nowrap}
.header-tools{display:flex;align-items:center;gap:18px}
.social{display:flex;gap:6px}
.social span{width:26px;height:26px;border-radius:50%;background:var(--blue)}
.social span:nth-child(2){background:var(--red)}
.social span:nth-child(3){background:var(--ink)}
.header-btn{font-size:11px;padding:6px 12px;background:var(--ink);color:var(--white);border-radius:2px}
.phone{text-align:right}
.phone small{display:block;font-size:10px;color:var(--mid)}
.phone strong{font-size:26px;font-weight:800;color:var(--ink)}

/* nav */
.main-nav{height:48px;background:var(--white)}
.main-nav .container{height:48px;background:var(--ink);display:flex;align-items:center;padding:0 14px}
.main-nav a{color:var(--white);font-size:12px;font-weight:600;padding:0 14px;line-height:48px;text-decoration:none}
.main-nav a.active{background:var(--blue)}
.nav-search{margin-left:auto;display:flex;align-items:center;gap:8px}
.nav-search span{width:180px;height:24px;background:#3a3b40;color:var(--mid);font-size:11px;padding:4px 8px}
.nav-search b{background:var(--blue);color:var(--white);font-size:11px;padding:5px 12px}

/* hero */
.hero{height:272px;background:linear-gradient(180deg,#2b2a5c 0%,#5b4f8f 45%,#a894b5 70%,#4e4663 100%);position:relative}
.hero .container{padding-top:70px}
.hero .eyebrow{color:var(--white)}
.hero h1{font-size:46px;font-weight:300;color:var(--white);line-height:1.05;text-transform:uppercase;width:560px;margin-top:6px}
.hero-dots{display:flex;gap:6px;margin-top:18px}
.hero-dots span{width:8px;height:8px;border-radius:50%;background:rgba(255,255,255,.5)}
.hero-dots span:first-child{background:var(--white)}

/* sectors */
.sectors{height:340px;background:linear-gradient(135deg,#1b1c22,#2c2d36 60%,#1a1b1f)}
.sector-grid{display:grid;grid-template-columns:260px 260px 260px;grid-auto-rows:150px;gap:12px;padding-top:14px}
.sector{position:relative;padding:12px}
.sector.wide{grid-column:span 2}
.sector h3{font-size:15px;font-weight:600;color:var(--white);text-transform:uppercase;line-height:1.1;width:120px}
.sector .btn{position:absolute;left:12px;bottom:12px}
.s1{background:linear-gradient(160deg,#2e4f78,#101a2c)}
.s2{background:linear-gradient(160deg,#b58a3c,#3b2a12)}
.s3{background:linear-gradient(160deg,#c2a25a,#4a3315)}
.s4{background:linear-gradient(160deg,#6a6f7a,#23262d)}
.s5{background:linear-gradient(160deg,#3e6ea7,#0f1d33)}

/* welcome */
.welcome{height:420px;padding-top:40px}
.welcome .container{display:flex;justify-content:space-between}
.welcome-copy{width:640px}
.welcome-copy h2{font-size:30px;font-weight:300;color:var(--ink);line-height:1.1;text-transform:uppercase;margin:4px 0 14px}
.welcome-copy h2 b{font-weight:400;color:var(--blue)}
.welcome-copy p{font-size:11px;line-height:1.6;margin-bottom:10px}
.welcome-copy h4{font-size:12px;font-weight:700;color:var(--ink);margin-bottom:6px}
.welcome-copy ul{font-size:11px;line-height:1.6;margin:0 0 10px 18px}
.promo{width:240px;height:330px;position:relative;padding:14px;background:linear-gradient(180deg,#e9e4d9,#b9b2a3)}
.promo-photo{position:absolute;inset:0 0 110px 0;background:linear-gradient(180deg,#d9d3c5,#a8a091)}
.promo-copy{position:absolute;left:14px;right:14px;bottom:40px;color:var(--ink)}
.promo-copy strong{display:block;font-size:16px;font-weight:700}
.promo-copy .big{font-size:42px;font-weight:800;color:var(--red);line-height:1}
.promo .btn{position:absolute;left:14px;bottom:12px}
.promo .arrow{position:absolute;right:14px;bottom:12px;width:24px;height:24px;background:var(--ink)}

/* products */
.products{height:340px;background:var(--grey);padding-top:24px}
.section-head{display:flex;justify-content:space-between;align-items:flex-end;margin-bottom:18px}
.arrows{display:flex;gap:6px}
.arrows span{width:26px;height:26px;background:var(--ink);display:flex;align-items:center;justify-content:center}
.product-grid{display:grid;grid-template-columns:repeat(4,1fr);gap:24px}
.product-shot{height:150px;background:radial-gradient(circle at 50% 45%,#6d6f74 0,#1a1a1c 45%,#000 100%)}
.product-info{background:var(--white);padding:10px 12px}
.product-info h5{font-size:12px;font-weight:700;color:var(--ink)}
.price{font-size:22px;font-weight:700;color:var(--blue)}
.price s{font-size:12px;color:var(--mid);font-weight:400;margin-left:6px}

/* video */
.video{height:360px;background:var(--grey);padding-top:10px}
.video-frame{height:260px;margin-top:16px;background:linear-gradient(180deg,#7ea0c6 0%,#a9bdd4 50%,#6e6a5e 100%);position:relative}
.video-frame svg{position:absolute;left:50%;top:50%;transform:translate(-50%,-50%)}

/* more videos */
.more-videos{height:180px;background:var(--grey);padding-top:10px}
.more-videos .eyebrow{margin-bottom:10px}
.clip-grid{display:grid;grid-template-columns:repeat(4,1fr);gap:24px}
.clip{height:120px;background:var(--ink);display:flex;flex-direction:column;align-items:center;justify-content:center;gap:8px;color:var(--white);text-align:center}
.clip p{font-size:11px;font-weight:700;line-height:1.2;text-transform:uppercase}

/* cta */
.cta{height:220px;background:var(--blue);position:relative;overflow:hidden}
.cta-photo{position:absolute;right:0;top:0;width:560px;height:220px;background:linear-gradient(90deg,var(--blue) 0%,#8fb8cc 25%,#c8d3d8 60%,#9aa6ad 100%)}
.cta .container{padding-top:30px}
.cta .eyebrow{color:var(--white);font-size:11px}
.cta h2{font-size:38px;font-weight:300;color:var(--white);line-height:1.05;text-transform:uppercase;margin:6px 0 8px;width:420px}
.cta p{font-size:11px;color:var(--white);width:380px;margin-bottom:12px}

/* footer */
.site-footer{height:200px;background:var(--dark);padding-top:40px}
.site-footer .container{display:grid;grid-template-columns:250px 250px 1fr;gap:30px}
.footer-social{display:flex;gap:10px}
.footer-social span{width:42px;height:42px;border-radius:50%;background:var(--blue)}
.footer-social span:nth-child(2){background:var(--red)}
.footer-social span:nth-child(3){background:#c63b2f}
.site-footer h6{font-size:12px;font-weight:700;color:var(--white);text-transform:uppercase;margin-bottom:12px}
.site-footer li{list-style:none;font-size:11px;color:#c5c7cb;line-height:1.8}
.site-footer li:first-child{color:var(--blue)}
.site-footer p{font-size:10px;color:#9a9da3;line-height:1.5;margin-bottom:10px}
.signup{display:flex}
.signup span{flex:1;height:28px;background:var(--white);font-size:11px;color:var(--mid);padding:6px 10px}
.signup b{width:34px;height:28px;background:var(--blue)}

/* bottom bar */
.bottom-bar{height:100px}
.bottom-bar .container{height:100px;display:flex;align-items:center;gap:28px}
.bottom-bar .brand-square{width:28px;height:28px}
.bottom-bar .brand-name{font-size:20px}
.copyright{font-size:10px;color:var(--mid);line-height:1.5}
.cards{margin-left:auto;display:flex;gap:6px}
.cards span{width:40px;height:26px;border-radius:3px;background:#dfe1e4}
</style>
</head>
<body>

<header class="site-header">
  <div class="container">
    <div class="brand">
      <span class="brand-square"></span>
      <span class="brand-name">Lumvale</span>
    </div>
    <div class="header-tools">
      <div class="social"><span></span><span></span><span></span></div>
      <span class="header-btn">Request a Quote</span>
      <span class="header-btn">My Account</span>
      <div class="phone"><small>Call us today</small><strong>1-800-555-0148</strong></div>
    </div>
  </div>
</header>

<nav class="main-nav">
  <div class="container">
    <a class="active">HOME</a><a>ABOUT US</a><a>CONTACT US</a><a>BLOG</a>
    <div class="nav-search"><span>Search</span><b>Get Quote</b></div>
  </div>
</nav>

<section class="hero" role="img" aria-label="Car park at dusk lit by LED street lights">
  <div class="container">
    <div class="eyebrow">Car Park Lighting</div>
    <h1>Commercial Lighting using LED Retrofit Lights</h1>
    <div class="hero-dots"><span></span><span></span></div>
  </div>
</section>

<section class="sectors">
  <div class="container sector-grid">
    <div class="sector s1" role="img" aria-label="Lit car park at night"><h3>Car Park Lighting</h3><span class="btn">Read More</span></div>
    <div class="sector s2" role="img" aria-label="Lit school hall"><h3>Educational Lighting</h3><span class="btn">Read More</span></div>
    <div class="sector s3" role="img" aria-label="Warm restaurant interior"><h3>Hospitality Lighting</h3><span class="btn">Read More</span></div>
    <div class="sector s4" role="img" aria-label="Modern office interior"><h3>Office Lighting</h3><span class="btn">Read More</span></div>
    <div class="sector s5 wide" role="img" aria-label="Warehouse with high bay lights"><h3>Warehouse Lighting</h3><span class="btn">Read More</span></div>
  </div>
</section>

<section class="welcome">
  <div class="container">
    <div class="welcome-copy">
      <div class="eyebrow">Welcome to</div>
      <h2>The commercial lighting division of <b>Lumvale.</b></h2>
      <p>We help businesses cut power and maintenance costs with quality induction and LED lighting. Our team works with owners, managers and contractors to plan, supply and install the right lights for every site, big or small, across the country.</p>
      <h4>WE MAKE IT AN EASY PROCESS BY PROVIDING YOU WITH:</h4>
      <ul>
        <li>A free site review and a clear lighting plan for your space</li>
        <li>Honest savings figures on power and upkeep over time</li>
        <li>Trusted products backed by long warranties and local support</li>
      </ul>
      <p>Browse our car park, school, hospitality, office and warehouse ranges to find lights suited to your needs, or speak with our team about a custom plan for your site.</p>
      <p>With a wide range in stock and fast delivery, we can help your project move ahead quickly. <b>Request a quote today.</b></p>
    </div>
    <aside class="promo">
      <div class="promo-photo" role="img" aria-label="Stack of boxed lamps on sale"></div>
      <div class="promo-copy"><strong>CLEARANCE SALE</strong><span class="big">50% OFF</span></div>
      <span class="btn">Shop Now</span><span class="arrow"></span>
    </aside>
  </div>
</section>

<section class="products">
  <div class="container">
    <div class="section-head">
      <div><div class="eyebrow">Suitable</div><div class="heading">Products</div></div>
      <div class="arrows">
        <span><svg width="10" height="10" viewBox="0 0 10 10"><path d="M7 1 3 5l4 4" stroke="#fff" stroke-width="2" fill="none"/></svg></span>
        <span><svg width="10" height="10" viewBox="0 0 10 10"><path d="M3 1l4 4-4 4" stroke="#fff" stroke-width="2" fill="none"/></svg></span>
      </div>
    </div>
    <div class="product-grid">
      <div><div class="product-shot" role="img" aria-label="LED bulb"></div><div class="product-info"><h5>6W BRITEON LED</h5><div class="price">$99<s>$120</s></div></div></div>
      <div><div class="product-shot" role="img" aria-label="LED downlight"></div><div class="product-info"><h5>6W BRITEON LED</h5><div class="price">$99<s>$120</s></div></div></div>
      <div><div class="product-shot" role="img" aria-label="LED flood light"></div><div class="product-info"><h5>6W BRITEON LED</h5><div class="price">$99<s>$120</s></div></div></div>
      <div><div class="product-shot" role="img" aria-label="LED spot lamp"></div><div class="product-info"><h5>6W BRITEON LED</h5><div class="price">$99<s>$120</s></div></div></div>
    </div>
  </div>
</section>

<section class="video">
  <div class="container">
    <div class="eyebrow">Our</div>
    <div class="heading">Video</div>
    <div class="video-frame" role="img" aria-label="Installer on a lift fitting a street light among trees">
      <svg width="70" height="70" viewBox="0 0 70 70"><circle cx="35" cy="35" r="33" fill="rgba(0,0,0,.55)"/><path d="M28 22v26l20-13z" fill="#fff"/></svg>
    </div>
  </div>
</section>

<section class="more-videos">
  <div class="container">
    <div class="eyebrow">View Our Install Videos</div>
    <div class="clip-grid">
      <div class="clip"><svg width="30" height="30" viewBox="0 0 30 30"><circle cx="15" cy="15" r="14" fill="#33a6d7"/><path d="M12 9v12l9-6z" fill="#fff"/></svg><p>1000W Shoe<br>Box Install</p></div>
      <div class="clip"><svg width="30" height="30" viewBox="0 0 30 30"><circle cx="15" cy="15" r="14" fill="#33a6d7"/><path d="M12 9v12l9-6z" fill="#fff"/></svg><p>400W Up<br>Light Video</p></div>
      <div class="clip"><svg width="30" height="30" viewBox="0 0 30 30"><circle cx="15" cy="15" r="14" fill="#33a6d7"/><path d="M12 9v12l9-6z" fill="#fff"/></svg><p>1000W Shoe<br>Box Install</p></div>
      <div class="clip"><svg width="30" height="30" viewBox="0 0 30 30"><circle cx="15" cy="15" r="14" fill="#33a6d7"/><path d="M12 9v12l9-6z" fill="#fff"/></svg><p>400W Up<br>Light Video</p></div>
    </div>
  </div>
</section>

<section class="cta">
  <div class="cta-photo" role="img" aria-label="Technician checking a ceiling light fitting"></div>
  <div class="container">
    <div class="eyebrow">Search for a modern lighting option?</div>
    <h2>You're in the right place!</h2>
    <p>Talk with our lighting team today and find the best way to save on your power bills.</p>
    <span class="btn">Read More</span>
  </div>
</section>

<footer class="site-footer">
  <div class="container">
    <div class="footer-social"><span></span><span></span><span></span></div>
    <div>
      <h6>Additional Links</h6>
      <ul><li>Home</li><li>About Us</li><li>Contact Us</li><li>Blog</li></ul>
    </div>
    <div>
      <h6>Join Our Newsletter</h6>
      <p>Sign up for news on new products, lighting tips and special offers sent straight to your inbox each month.</p>
      <div class="signup"><span>Email Address</span><b></b></div>
    </div>
  </div>
</footer>

<div class="bottom-bar">
  <div class="container">
    <div class="brand"><span class="brand-square"></span><span class="brand-name">Lumvale</span></div>
    <div class="copyright">Copyright © 2015 Lumvale<br>All rights reserved.</div>
    <div class="cards"><span></span><span></span><span></span><span></span><span></span></div>
  </div>
</div>

</body>
</html>
```